Business Card Design

We would like a business card that utilizes our current logo and keeps with the same feel - elegant and organic. Our farm isn't about mass production, it's about excellence, education, beautiful events and flowers - people, culture, and community.

Target Market(s)

Patrons to our farm who are interested in weddings, events, or our flowers and vegetables.

Contact Information for Business Card

Name, address, cell email (Danielle Hoskins, 2716 Wrenfield Rd, Brennick, CO 80617, cell 30.412.6638, email danielle@wrenfieldacres.com)

```html
<!DOCTYPE html>
<html lang="en">
<head>
<meta charset="utf-8">
<title>Wrenfield Acres — Business Card</title>
<link rel="stylesheet" href="https://fonts.googleapis.com/css2?family=EB+Garamond:ital,wght@0,400;1,400&family=Lato:wght@400;700&display=swap">
<style>
  :root {
    --backdrop: #ababab;
    --card-dark: #191b1a;
    --card-light: #ffffff;
    --sage: #6d8572;
    --sage-deep: #5b6b5e;
    --contact: #6f7f73;
    --clay: #a57a58;
    --url-grey: #6a6d6b;
  }
  * { margin: 0; padding: 0; box-sizing: border-box; }
  html, body { width: 1200px; height: 1000px; overflow: hidden; }
  body { background: var(--backdrop); position: relative; font-family: Arial, Helvetica, sans-serif; }

  .card {
    position: absolute;
    left: 294px;
    width: 613px;
    height: 352px;
    border-radius: 22px;
    overflow: hidden;
  }
  .card--front { top: 118px; background: var(--card-dark); }
  .card--back { top: 530px; background: var(--card-light); }

  .brand-name {
    position: absolute;
    left: 0; right: 0;
    top: 140px;
    text-align: center;
    font-family: "EB Garamond", Georgia, serif;
    font-weight: 400;
    font-size: 64px;
    line-height: 1;
    color: var(--sage);
    letter-spacing: 1px;
  }
  .website {
    position: absolute;
    left: 0; right: 0;
    top: 294px;
    text-align: center;
    font-family: "Lato", Arial, sans-serif;
    font-size: 14px;
    letter-spacing: 0.6px;
    color: var(--url-grey);
  }

  .person-name {
    position: absolute;
    left: 80px;
    top: 138px;
    font-family: "EB Garamond", Georgia, serif;
    font-style: italic;
    font-weight: 400;
    font-size: 42px;
    color: var(--sage-deep);
    line-height: 1.2;
  }
  .address {
    position: absolute;
    left: 81px;
    top: 199px;
    font-size: 16px;
    line-height: 19px;
    color: var(--contact);
    font-style: normal;
  }
  .contact-list {
    position: absolute;
    left: 78px;
    top: 266px;
    list-style: none;
    font-size: 16px;
    line-height: 21px;
    color: var(--contact);
  }
  .contact-list li { display: flex; align-items: center; gap: 8px; }
  .contact-list svg { width: 13px; height: 11px; flex: none; }

  .brand-mark-small {
    position: absolute;
    right: 58px;
    top: 276px;
    font-family: "EB Garamond", Georgia, serif;
    font-weight: 400;
    font-size: 26px;
    color: var(--sage);
  }
</style>
</head>
<body>
  <section class="card card--front" aria-label="Card front">
    <p class="brand-name">Wrenfield Acres</p>
    <p class="website">wrenfieldacres.com</p>
  </section>

  <section class="card card--back" aria-label="Card back">
    <h1 class="person-name">Danielle Hoskins</h1>
    <address class="address">2716 Wrenfield Rd<br>Brennick, CO 80617</address>
    <ul class="contact-list">
      <li>
        <svg viewBox="0 0 13 11" aria-hidden="true"><path fill="var(--clay)" d="M3 0.5 L5 2.8 L3.8 4 Q5.2 6.6 7.8 7.6 L9 6.4 L11.5 8.4 L10.2 10.3 Q4.5 10 1.6 2.2 Z"/></svg>
        <span>30.412.6638</span>
      </li>
      <li>
        <svg viewBox="0 0 13 11" aria-hidden="true"><rect x="0.5" y="1.5" width="12" height="8" fill="var(--clay)"/><path d="M0.8 1.8 L6.5 6 L12.2 1.8" fill="none" stroke="#fff" stroke-width="0.9"/></svg>
        <span>danielle@wrenfieldacres.com</span>
      </li>
    </ul>
    <p class="brand-mark-small">Wrenfield Acres</p>
  </section>
</body>
</html>
```